Go Marsh Florida Business Website Branding

Looking for a wordpress template design with CSS and HTML encoding. Current website can be seen at gomarshfloridaxq.com.

WE ARE CURRENTLY IN PROCESS GETTING A LOGO DESIGN... I HAVE INCLUDED THE TOP POTENTIAL DESIGNS FOR REFERENCE TO HELP UNDERSTAND WHAT STYLE WE ARE LOOKING FOR...
NOTE: THE “PALM RIDERS” LOGO WAS A PREVIOUS COMPANY WE OWNED SO YOU CAN GE A FEEL FOR THE TYPE OF DESIGNS WE HAVE USED IN THE PAST.

My blog will focus on making a connection with wild Florida, it’s wildlife, plants and animals... with an eye toward Florida conservation, nature adventure trips, and education... Content, photos and other merchandise will also be offered for sale.
I’m looking for a site design that incorporates Florida nature and wildlife/plants, with a fun “Old Florida” retro-adventure feel.
When they see this site it should speak to the import of natural Florida and the critical nature of the ecosystem here... while being instantly recognizable and iconic... IE: when I think of florida I think of water, plants, warmth, sunsets etc...

https://join.chatvorahub.com/t/kelvoranetwo-xqr7381/shared_invite/qa-pmlun58d-rTbWoHkcNmsfJY4a9Xe2Pd

Target Market(s)

Nature, Education, Conservation, Photography

Industry/Entity Type

Photographer

Coding

Coded - Design and coding required

Requirements
Must have
• Need to have site wide template design which generally includes a landing page and a general page template for other pages... Must include html and css encoding...
Should not have
• Any animals included in the site should be Florida native... IE: no African animals etc... This will require some research to ensure that if animals are included that they are part of the Florida ecosystem.

```html
<!DOCTYPE html>
<html lang="en">
<head>
<meta charset="utf-8">
<title>Go Marsh Florida</title>
<link href="https://fonts.googleapis.com/css2?family=Lato:ital,wght@0,400;0,700;0,900;1,400&family=Yellowtail&display=swap" rel="stylesheet">
<style>
:root{
  --orange:#ef8a2d;
  --orange-deep:#d9631b;
  --cream:#f8f5e6;
  --ink:#2f2f2f;
  --text:#5a5a5a;
  --muted:#8a8a8a;
  --footer:#333333;
  --white:#ffffff;
}
*{margin:0;padding:0;box-sizing:border-box}
html,body{width:1200px;height:4563px;overflow:hidden;background:var(--cream)}
body{font-family:'Lato',sans-serif;color:var(--text)}
.page{position:relative;width:1200px;height:4563px;overflow:hidden;background:var(--cream)}
.abs{position:absolute}
.script{font-family:'Yellowtail',cursive;color:var(--ink);font-weight:400;white-space:nowrap}
.btn{position:absolute;background:var(--orange);color:var(--white);font-weight:700;font-size:14px;text-transform:uppercase;display:flex;align-items:center;justify-content:center;gap:10px;border-radius:3px}
.btn .dot{width:13px;height:13px;border-radius:50%;background:var(--white);position:relative}
.btn .dot::after{content:"";position:absolute;left:4px;top:3.5px;border-left:5px solid var(--orange);border-top:3px solid transparent;border-bottom:3px solid transparent}

/* header */
.site-header{position:absolute;left:0;top:0;width:1200px;height:74px;background:var(--white);z-index:5}
.brand{position:absolute;left:110px;top:20px;display:flex;align-items:center;gap:10px;font-weight:900;font-size:19px;color:var(--orange-deep)}
.brand .mark{width:22px;height:22px;border-radius:50%;background:var(--orange)}
.nav{position:absolute;top:28px;font-size:14px;font-weight:700;color:var(--ink);text-transform:uppercase}
.nav.active{color:var(--orange)}
.login{left:978px;top:17px;width:109px;height:43px}
.lock{width:10px;height:9px;background:var(--white);border-radius:1px;position:relative;margin-top:4px}
.lock::before{content:"";position:absolute;left:1.5px;top:-6px;width:5px;height:6px;border:1.5px solid var(--white);border-bottom:none;border-radius:4px 4px 0 0}

/* hero */
.hero-photo{left:0;top:74px;width:1200px;height:600px;background:linear-gradient(180deg,#9fc3e6 0%,#c9dcea 22%,#7f9bb5 34%,#5d7fa0 55%,#8aa6c1 78%,#4e6f8e 100%)}
.hero-title{left:106px;top:240px;font-size:80px;color:var(--white)}
.hero-lede{left:112px;top:350px;width:500px;font-size:16px;line-height:26px;color:var(--white)}
.get-started{left:112px;top:454px;width:152px;height:48px}

/* about */
.portrait{left:110px;top:803px;width:442px;height:442px;border-radius:50%;border:10px solid var(--orange);background:radial-gradient(circle at 50% 40%,#e6a36f 0%,#b5763f 45%,#6a8fa8 100%)}
.about-title{left:624px;top:780px;font-size:50px}
.about-copy{left:624px;top:856px;width:461px;font-size:14.6px;line-height:27.5px;text-align:justify}
.read-more{left:624px;top:1207px;width:152px;height:46px}

/* eco */
.eco-photo{left:0;top:1340px;width:1200px;height:780px;background:linear-gradient(180deg,#3a3d32 0%,#4c5040 35%,#2f3329 70%,#23261f 100%)}
.eco-title{left:0;top:1460px;width:1200px;text-align:center;font-size:54px;color:var(--white)}
.eco-img{top:1581px;width:312px;height:214px;border:3px solid rgba(255,255,255,.7)}
.eco-head{top:1820px;font-size:14px;font-weight:700;color:var(--white);text-transform:uppercase}
.eco-text{top:1848px;width:270px;font-size:14px;line-height:26px;color:var(--white)}

/* blog */
.blog-title{left:0;top:2120px;width:1200px;text-align:center;font-size:54px}
.blog-card{top:2244px;width:478px;height:284px;background:var(--white);box-shadow:0 2px 8px rgba(0,0,0,.12);padding:4px}
.blog-img{width:100%;height:100%}
.blog-head{top:2556px;width:420px;font-size:13.5px;font-weight:700;line-height:20px;color:var(--ink);text-transform:uppercase}
.blog-rule{top:2614px;width:424px;height:1px;background:#e1ddcc}
.blog-meta{top:2634px;width:424px;display:flex;align-items:center;font-size:14px;color:var(--muted)}
.blog-meta .item{display:flex;align-items:center;gap:12px;margin-right:38px}
.blog-meta .go{margin-left:auto}

/* testimonials */
.testi-bg{left:0;top:2700px;width:1200px;height:640px;background:linear-gradient(180deg,#ef8e3a 0%,#e98a3a 50%,#d9782c 100%)}
.testi-title{left:0;top:2838px;width:1200px;text-align:center;font-size:54px;color:var(--white)}
.testi-card{top:2935px;width:317px;height:237px;background:var(--white);padding:22px 14px;box-shadow:0 2px 10px rgba(0,0,0,.15)}
.testi-card.featured{background:var(--orange)}
.testi-card p{margin-top:22px;font-size:13.5px;font-style:italic;line-height:23px;color:var(--muted)}
.testi-card.featured p,.testi-card.featured .who b,.testi-card.featured .who span{color:var(--white)}
.who{position:absolute;left:14px;top:170px;display:flex;align-items:center;gap:20px}
.avatar{width:50px;height:50px;border-radius:50%;background:linear-gradient(135deg,#c9c9c9,#7d8a99)}
.who b{display:block;font-size:13.5px;color:var(--orange);text-transform:uppercase;font-weight:700}
.who span{font-size:13.5px;color:var(--muted)}

/* instagram */
.insta-title{left:0;top:3340px;width:1200px;text-align:center;font-size:54px}
.tile{position:absolute}

/* footer */
.foot-logo{left:124px;top:4284px;font-size:20px;font-weight:900;color:var(--orange);display:flex;align-items:center;gap:10px}
.foot-logo .mark{width:20px;height:20px;border-radius:50%;background:var(--orange)}
.foot-about{left:122px;top:4362px;width:262px;font-size:14px;line-height:30px;color:var(--white);text-align:justify}
.foot-col h4{font-size:14px;font-weight:700;text-decoration:underline;color:var(--white);text-transform:uppercase;margin-bottom:12px}
.foot-col li{list-style:none;font-size:13px;color:var(--white);height:34.5px;display:flex;align-items:center;gap:12px}
.foot-col li::before{content:"»";color:var(--white);font-size:14px}
.contact li::before{content:none}
.cicon{width:30px;height:30px;border-radius:50%;background:var(--white);display:flex;align-items:center;justify-content:center;flex:none}
.contact li{height:auto;margin-bottom:18px;align-items:flex-start;gap:20px;line-height:22px}
.foot-rule{left:110px;top:4493px;width:978px;height:1px;background:#6a6a6a}
.copyright{left:110px;top:4514px;font-size:14px;color:var(--white)}
.social{top:4507px;width:34px;height:34px;border-radius:50%;border:1.5px solid var(--white)}
</style>
</head>
<body>
<div class="page">

  <header class="site-header">
    <div class="brand"><span class="mark"></span>Go Marsh Florida</div>
    <div class="nav active" style="left:376px">Home</div>
    <div class="nav" style="left:454px">About Us</div>
    <div class="nav" style="left:560px">Adventures</div>
    <div class="nav" style="left:689px">Recent Blog</div>
    <div class="nav" style="left:821px">Contact Us</div>
    <div class="btn login">Log In <span class="lock"></span></div>
  </header>

  <!-- hero -->
  <div class="abs hero-photo" role="img" aria-label="Lakeside city skyline with palm trees, lawn and two swans on calm water"></div>
  <svg class="abs" style="left:0;top:470px" width="1200" height="220" viewBox="0 0 1200 220">
    <path d="M0 130 C120 200 260 210 430 170 C640 120 820 50 1000 40 C1100 34 1160 40 1200 50 L1200 220 L0 220 Z" fill="#d9631b"/>
    <path d="M0 150 C130 210 280 218 450 180 C650 135 830 70 1010 60 C1110 55 1170 62 1200 70 L1200 220 L0 220 Z" fill="#ef8a2d"/>
    <path d="M0 170 C140 220 300 226 470 192 C660 150 840 90 1020 80 C1115 75 1170 82 1200 90 L1200 220 L0 220 Z" fill="#f8f5e6"/>
  </svg>
  <div class="abs script hero-title">Go Marsh Florida</div>
  <p class="abs hero-lede">Come explore wild places and stunning scenery with me as I discover new and exciting eco-adventures and learn about the rare and unique wildlife and environments</p>
  <div class="btn get-started">Get Started <span class="dot"></span></div>

  <!-- about -->
  <div class="abs portrait" role="img" aria-label="Portrait of the naturalist at the beach at sunset"></div>
  <h2 class="abs script about-title">About Me</h2>
  <p class="abs about-copy">Hello nature lovers! I'm Maren Calloway, a wildlife educator, Sunshine State Naturalist, nature writer and photographer, busy mama of three kiddos, a playful Havanese puppy, two very chubby guinea pigs, and a giant tree frog. I have a passion for all things nature and I adore living in Southwest Florida. I will always be a California girl, but from the moment I set foot in Florida, its wild beauty stole my heart. For the past 23 years, I have been fortunate to have some very unique and special experiences caring for many different species of animals and educating the public about wildlife and the environment. My hope is that those I endeavor to educate will better understand their connection with the natural world and our shared responsibility to protect Florida's wild and priceless beauty.</p>
  <div class="btn read-more">Read More <span class="dot"></span></div>

  <!-- eco adventures -->
  <div class="abs eco-photo" role="img" aria-label="Misty pine forest at dusk"></div>
  <svg class="abs" style="left:0;top:1330px" width="1200" height="110" viewBox="0 0 1200 110">
    <path d="M0 0 L1200 0 L1200 40 C1130 60 1060 110 960 100 C820 86 700 40 520 38 C320 36 150 80 0 90 Z" fill="#f8f5e6"/>
    <path d="M0 90 C150 80 320 36 520 38 C700 40 820 86 960 100 C1060 110 1130 60 1200 40 L1200 52 C1130 72 1060 120 960 110 C820 96 700 52 520 50 C320 48 150 92 0 102 Z" fill="#d9631b"/>
  </svg>
  <svg class="abs" style="left:0;top:1960px" width="1200" height="170" viewBox="0 0 1200 170">
    <path d="M0 120 C200 150 330 150 470 110 C640 60 780 20 960 20 C1080 20 1160 40 1200 60 L1200 170 L0 170 Z" fill="#d9631b"/>
    <path d="M0 134 C200 164 330 164 470 124 C640 74 780 34 960 34 C1080 34 1160 54 1200 74 L1200 170 L0 170 Z" fill="#f8f5e6"/>
  </svg>
  <h2 class="abs script eco-title">Eco – Adventures</h2>
  <div class="abs eco-img" style="left:110px;background:linear-gradient(135deg,#b14a3e,#e0556a 40%,#6f8a3b 70%,#c9cf43)" role="img" aria-label="Red and yellow pine lily blossom"></div>
  <div class="abs eco-img" style="left:443px;background:linear-gradient(135deg,#6d5c43,#cfc2a6 45%,#8c7655 80%)" role="img" aria-label="White peacock butterfly on dry leaves"></div>
  <div class="abs eco-img" style="left:778px;background:linear-gradient(135deg,#5d7b36,#9b6bb3 45%,#6f8c3e 85%)" role="img" aria-label="Purple blazing star wildflower"></div>
  <div class="abs eco-head" style="left:124px">Lorem ipsum dolor sit</div>
  <div class="abs eco-head" style="left:458px">Lorem ipsum dolor sit</div>
  <div class="abs eco-head" style="left:792px">Lorem ipsum dolor sit</div>
  <p class="abs eco-text" style="left:124px">Lorem ipsum dolor sit amet, consectetur adipiscing elit, sed do eiusmod tempor incididunt ut labore et dolore magna</p>
  <p class="abs eco-text" style="left:458px">Lorem ipsum dolor sit amet, consectetur adipiscing elit, sed do eiusmod tempor incididunt ut labore et dolore magna</p>
  <p class="abs eco-text" style="left:792px">Lorem ipsum dolor sit amet, consectetur adipiscing elit, sed do eiusmod tempor incididunt ut labore et dolore magna</p>

  <!-- blog -->
  <h2 class="abs script blog-title">Latest Blog</h2>
  <div class="abs blog-card" style="left:110px"><div class="blog-img" style="background:linear-gradient(135deg,#6c6a5e,#3a3733 40%,#9a9588 75%,#c9c4b5)" role="img" aria-label="Trail sign warning about black bears"></div></div>
  <div class="abs blog-card" style="left:610px"><div class="blog-img" style="background:linear-gradient(90deg,#d9dde4,#8fa6c2 35%,#e5e6ea 55%,#3e6fa8 80%,#d6dae2)" role="img" aria-label="Information boards at a nature preserve trailhead"></div></div>
  <div class="abs blog-head" style="left:138px">Sunshine State Naturalist Uplands Nature Journal</div>
  <div class="abs blog-head" style="left:637px">Sunshine State Naturalist Uplands Nature Journal</div>
  <div class="abs blog-rule" style="left:138px"></div>
  <div class="abs blog-rule" style="left:637px"></div>
  <div class="abs blog-meta" style="left:138px">
    <span class="item"><svg width="14" height="14" viewBox="0 0 14 14"><rect x="1" y="3" width="12" height="10" fill="none" stroke="#ef8a2d" stroke-width="1.5"/><path d="M1 6h12M4 1v3M10 1v3" stroke="#ef8a2d" stroke-width="1.5"/></svg>12 Oct 2020</span>
    <span class="item"><svg width="14" height="14" viewBox="0 0 14 14"><circle cx="7" cy="4.5" r="3" fill="none" stroke="#ef8a2d" stroke-width="1.5"/><path d="M1.5 13c0-3 2.5-5 5.5-5s5.5 2 5.5 5" fill="none" stroke="#ef8a2d" stroke-width="1.5"/></svg>Maren</span>
    <span class="item"><svg width="16" height="14" viewBox="0 0 16 14"><path d="M2 2h12v7H7l-3 3V9H2z" fill="none" stroke="#ef8a2d" stroke-width="1.5"/></svg>36523</span>
    <span class="go"><svg width="14" height="14" viewBox="0 0 14 14"><circle cx="7" cy="7" r="7" fill="#ef8a2d"/><path d="M5.5 4l3.5 3-3.5 3" fill="none" stroke="#fff" stroke-width="1.6"/></svg></span>
  </div>
  <div class="abs blog-meta" style="left:637px">
    <span class="item"><svg width="14" height="14" viewBox="0 0 14 14"><rect x="1" y="3" width="12" height="10" fill="none" stroke="#ef8a2d" stroke-width="1.5"/><path d="M1 6h12M4 1v3M10 1v3" stroke="#ef8a2d" stroke-width="1.5"/></svg>12 Oct 2020</span>
    <span class="item"><svg width="14" height="14" viewBox="0 0 14 14"><circle cx="7" cy="4.5" r="3" fill="none" stroke="#ef8a2d" stroke-width="1.5"/><path d="M1.5 13c0-3 2.5-5 5.5-5s5.5 2 5.5 5" fill="none" stroke="#ef8a2d" stroke-width="1.5"/></svg>Maren</span>
    <span class="item"><svg width="16" height="14" viewBox="0 0 16 14"><path d="M2 2h12v7H7l-3 3V9H2z" fill="none" stroke="#ef8a2d" stroke-width="1.5"/></svg>36523</span>
    <span class="go"><svg width="14" height="14" viewBox="0 0 14 14"><circle cx="7" cy="7" r="7" fill="#ef8a2d"/><path d="M5.5 4l3.5 3-3.5 3" fill="none" stroke="#fff" stroke-width="1.6"/></svg></span>
  </div>

  <!-- testimonials -->
  <div class="abs testi-bg" role="img" aria-label="Golden grassland tinted orange"></div>
  <svg class="abs" style="left:0;top:2690px" width="1200" height="120" viewBox="0 0 1200 120">
    <path d="M0 0 L1200 0 L1200 40 C1100 60 1000 110 860 100 C700 88 560 30 380 28 C220 26 90 70 0 86 Z" fill="#f8f5e6"/>
    <path d="M0 86 C90 70 220 26 380 28 C560 30 700 88 860 100 C1000 110 1100 60 1200 40 L1200 54 C1100 74 1000 124 860 114 C700 102 560 44 380 42 C220 40 90 84 0 100 Z" fill="#d9631b"/>
  </svg>
  <svg class="abs" style="left:0;top:3200px" width="1200" height="140" viewBox="0 0 1200 140">
    <path d="M0 112 C140 80 260 60 420 80 C600 104 760 120 930 80 C1060 50 1150 30 1200 26 L1200 140 L0 140 Z" fill="#d9631b"/>
    <path d="M0 126 C140 94 260 74 420 94 C600 118 760 134 930 94 C1060 64 1150 44 1200 40 L1200 140 L0 140 Z" fill="#f8f5e6"/>
  </svg>
  <h2 class="abs script testi-title">Testimonials</h2>
  <div class="abs testi-card" style="left:112px">
    <svg width="26" height="20" viewBox="0 0 26 20"><path d="M0 10C0 4 4 0 9 0v4c-3 0-5 2-5 5h5v11H0zM14 10c0-6 4-10 9-10v4c-3 0-5 2-5 5h5v11h-9z" fill="#ef8a2d"/></svg>
    <p>Nature has been for me, as long as I remember, a source of solace, inspiration, adventure, and delight; a home, a teacher, a companion</p>
    <div class="who"><div class="avatar" role="img" aria-label="Client portrait"></div><div><b>Della Harrow</b><span>Businessman</span></div></div>
  </div>
  <div class="abs testi-card featured" style="left:441px">
    <svg width="26" height="20" viewBox="0 0 26 20"><path d="M0 10C0 4 4 0 9 0v4c-3 0-5 2-5 5h5v11H0zM14 10c0-6 4-10 9-10v4c-3 0-5 2-5 5h5v11h-9z" fill="#fff"/></svg>
    <p>Lorem ipsum dolor sit amet, consectetur dipiscing elit, sed do eiusmod tempor incididunt ut labore et dolore magna aliqua.</p>
    <div class="who"><div class="avatar" role="img" aria-label="Client portrait"></div><div><b>Conrad Ellery</b><span>Businessman</span></div></div>
  </div>
  <div class="abs testi-card" style="left:769px">
    <svg width="26" height="20" viewBox="0 0 26 20"><path d="M0 10C0 4 4 0 9 0v4c-3 0-5 2-5 5h5v11H0zM14 10c0-6 4-10 9-10v4c-3 0-5 2-5 5h5v11h-9z" fill="#ef8a2d"/></svg>
    <p>Lorem ipsum dolor sit amet, consectetuadipiscing elit, sed do eiusmod tempor incididunt ut labore et dolore magna aliqua.</p>
    <div class="who"><div class="avatar" role="img" aria-label="Client portrait"></div><div><b>Tobias</b><span>Businessman</span></div></div>
  </div>

  <!-- instagram -->
  <h2 class="abs script insta-title">Follow Us On Instagram</h2>
  <div class="tile" style="left:110px;top:3477px;width:319px;height:222px;background:linear-gradient(180deg,#c9c9b4,#6f7d52 45%,#7a5a3a 70%,#5e6d3f)" role="img" aria-label="Horse and foal by a wooden fence"></div>
  <div class="tile" style="left:110px;top:3709px;width:319px;height:222px;background:linear-gradient(135deg,#8f8c86,#6d6a64 50%,#a4a09a)" role="img" aria-label="Animal track in sand"></div>
  <div class="tile" style="left:438px;top:3477px;width:321px;height:454px;background:radial-gradient(circle at 50% 45%,#f2b51a 0%,#d99a12 20%,#4f5e36 45%,#2f3a24 100%)" role="img" aria-label="Yellow wildflower in bloom"></div>
  <div class="tile" style="left:769px;top:3477px;width:319px;height:222px;background:linear-gradient(135deg,#4c5a34,#a8ab9a 50%,#3d4a2b)" role="img" aria-label="Spanish moss hanging in green foliage"></div>
  <div class="tile" style="left:769px;top:3709px;width:319px;height:222px;background:linear-gradient(135deg,#b8b2a5,#5d5a52 45%,#1f1f1f 60%,#9a9488)" role="img" aria-label="Black vulture perched on a branch"></div>

  <!-- footer -->
  <svg class="abs" style="left:0;top:3990px" width="1200" height="573" viewBox="0 0 1200 573">
    <path d="M0 230 C200 210 360 200 540 140 C720 80 880 10 1040 10 C1120 10 1170 20 1200 30 L1200 573 L0 573 Z" fill="#d9631b"/>
    <path d="M0 250 C200 230 360 220 540 160 C720 100 880 30 1040 30 C1120 30 1170 40 1200 50 L1200 573 L0 573 Z" fill="#ef8a2d"/>
    <path d="M0 262 C200 242 360 232 540 172 C720 112 880 42 1040 42 C1120 42 1170 52 1200 62 L1200 573 L0 573 Z" fill="#333333"/>
  </svg>
  <div class="abs foot-logo"><span class="mark"></span>Go Marsh Florida</div>
  <p class="abs foot-about">Lorem ipsum dolor sit amet, consectetur adipiscing elit, sed do eiusmod tempor incididunt ut labore</p>
  <div class="abs foot-col" style="left:463px;top:4265px">
    <h4>Quick Links</h4>
    <ul><li>Home</li><li>About Me</li><li>Adventures</li><li>Reviews</li><li>Contact Us</li></ul>
  </div>
  <div class="abs foot-col" style="left:659px;top:4265px">
    <h4>Other Links</h4>
    <ul><li>FAQ</li><li>Help Service</li><li>Terms Of Use</li><li>Privacy Policy</li><li>Blog</li></ul>
  </div>
  <div class="abs foot-col contact" style="left:868px;top:4265px">
    <h4>Contact Us</h4>
    <ul>
      <li><span class="cicon"><svg width="12" height="16" viewBox="0 0 12 16"><path d="M6 0a6 6 0 0 1 6 6c0 4-6 10-6 10S0 10 0 6a6 6 0 0 1 6-6z" fill="#ef8a2d"/><circle cx="6" cy="6" r="2.2" fill="#fff"/></svg></span><span>639 , Nemo enim ipsam<br>United States</span></li>
      <li><span class="cicon"><svg width="14" height="14" viewBox="0 0 14 14"><path d="M3 0l3 3-2 2c1 2 3 4 5 5l2-2 3 3-2 3C6 14 0 8 0 2z" fill="#ef8a2d"/></svg></span><span style="margin-top:4px">1 888 888 888</span></li>
      <li><span class="cicon"><svg width="16" height="12" viewBox="0 0 16 12"><rect x="1" y="1" width="14" height="10" fill="none" stroke="#ef8a2d" stroke-width="1.5"/><path d="M1 1l7 6 7-6" fill="none" stroke="#ef8a2d" stroke-width="1.5"/></svg></span><span style="margin-top:4px">info@gomarshfloridaxq.com</span></li>
    </ul>
  </div>
  <div class="abs foot-rule"></div>
  <div class="abs copyright">© 2020 Go Marsh Florida. All Rights Reserved</div>
  <div class="abs social" style="left:958px" aria-label="Social link"></div>
  <div class="abs social" style="left:1006px" aria-label="Social link"></div>
  <div class="abs social" style="left:1054px" aria-label="Social link"></div>

</div>
</body>
</html>
```